I'm an electrician and the name of my company is called Brisk 'N' Bright Electrical. I require a professional business card that speaks to my clients, I also need it to be innovative and modern. We do maintenance & service work for domestic and commercial premises.

Industry/Entity Type

Electrical

Contact Information for Business Card

Must have the name of my company Brisk 'N' Bright Electrical, my name Darren Kolovich and my contact details 0427 318 592 and company email address Brisknbrightelectrical@quillpost.example and/or website Brisknbrightelectrical.example.au

Logo Text

Brisk 'N' Bright Electrical (If possible)

Colors
33a6d7
0592cd
3176b5

```html
<!DOCTYPE html>
<html lang="en">
<head>
<meta charset="utf-8">
<title>Brisk 'N' Bright Electrical – Business Card</title>
<link href="https://fonts.googleapis.com/css2?family=Montserrat:wght@500;600;700;800&display=swap" rel="stylesheet">
<style>
  :root {
    --page: #ffffff;
    --card: #3a3b3d;
    --accent: #e8562f;
    --decor: #754c3f;
    --ink: #ffffff;
    --rule: #ffffff;
  }
  * { box-sizing: border-box; margin: 0; padding: 0; }
  html, body { width: 1200px; height: 1000px; overflow: hidden; background: var(--page); }
  body { position: relative; font-family: "Montserrat", Arial, sans-serif; color: var(--ink); }

  .card { position: absolute; background: var(--card); overflow: hidden; }
  .card--front { left: 305px; top: 111px; width: 639px; height: 362px; }
  .card--back  { left: 305px; top: 521px; width: 643px; height: 367px; }

  .brand-decor {
    position: absolute; left: 0; top: 0; width: 330px; height: 362px;
    background: linear-gradient(100deg, var(--decor) 0%, var(--decor) 55%, rgba(117,76,63,0) 100%);
    opacity: .9;
  }

  .wordmark {
    position: absolute; display: flex; align-items: center; gap: 10px;
    font-weight: 800; color: var(--ink); text-transform: uppercase; line-height: 1.02;
  }
  .wordmark__dot { width: 14px; height: 14px; background: var(--accent); border-radius: 50%; flex: none; }
  .wordmark__name { display: block; }
  .wordmark__sub { display: block; letter-spacing: .42em; }

  .card--front .wordmark { right: 44px; top: 164px; font-size: 26px; }
  .card--front .wordmark__sub { font-size: 13px; text-align: right; }

  .web-line {
    position: absolute; right: 30px; top: 320px; display: flex; align-items: center; gap: 10px;
    font-size: 10px; font-weight: 700; letter-spacing: .16em; text-transform: uppercase;
  }
  .web-line::before, .web-line::after { content: ""; width: 34px; height: 1px; background: var(--rule); }

  .card--back .wordmark { left: 50%; transform: translateX(-50%); top: 68px; font-size: 34px; }
  .card--back .wordmark__sub { font-size: 16px; text-align: right; }

  .divider {
    position: absolute; left: 325px; top: 150px; width: 8px; height: 217px;
    background: linear-gradient(90deg, rgba(0,0,0,.12), rgba(0,0,0,0));
  }

  .person { position: absolute; left: 52px; top: 233px; width: 270px; text-align: center; }
  .person__name { font-size: 24px; font-weight: 600; }
  .person__role { margin-top: 4px; font-size: 10px; font-weight: 600; letter-spacing: .42em; }

  .contacts { position: absolute; left: 354px; top: 224px; list-style: none; }
  .contacts li { display: flex; align-items: center; gap: 10px; font-size: 11px; font-weight: 700; font-family: "Montserrat", Arial, sans-serif; }
  .contacts li + li { margin-top: 27px; }
  .contacts svg { width: 15px; height: 15px; fill: var(--ink); flex: none; }
</style>
</head>
<body>

<section class="card card--front">
  <div class="brand-decor" role="img" aria-label="Large faint brand symbol decoration"></div>
  <div class="wordmark">
    <span class="wordmark__dot"></span>
    <span>
      <span class="wordmark__name">Brisk 'N' Bright</span>
      <span class="wordmark__sub">Electrical</span>
    </span>
  </div>
  <p class="web-line">Brisknbrightelectrical.example.au</p>
</section>

<section class="card card--back">
  <div class="wordmark">
    <span class="wordmark__dot"></span>
    <span>
      <span class="wordmark__name">Brisk 'N' Bright</span>
      <span class="wordmark__sub">Electrical</span>
    </span>
  </div>
  <div class="divider"></div>
  <div class="person">
    <p class="person__name">Darren Kolovich</p>
    <p class="person__role">DIRECTOR</p>
  </div>
  <ul class="contacts">
    <li>
      <svg viewBox="0 0 24 24" aria-hidden="true"><path d="M6.6 10.8a15.1 15.1 0 0 0 6.6 6.6l2.2-2.2a1 1 0 0 1 1-.25 11.4 11.4 0 0 0 3.6.57 1 1 0 0 1 1 1V20a1 1 0 0 1-1 1A17 17 0 0 1 3 4a1 1 0 0 1 1-1h3.5a1 1 0 0 1 1 1c0 1.25.2 2.45.57 3.57a1 1 0 0 1-.25 1z"/></svg>
      <span>0427 318 592</span>
    </li>
    <li>
      <svg viewBox="0 0 24 24" aria-hidden="true"><path d="M2 5h20v14H2z M3.5 6.5v.3L12 13l8.5-6.2v-.3z" fill-rule="evenodd"/></svg>
      <span>Brisknbrightelectrical@quillpost.example</span>
    </li>
  </ul>
</section>

</body>
</html>
```